Dulwick Medical

Need smart and sleek business cards design for my medical distribution company. use logos attached.

add my details

Harriet Colbeck
Director/Sales Agent
harriet@dulwickmedical.com.au
0461 835 207

```html
<!DOCTYPE html>
<html lang="en">
<head>
<meta charset="utf-8">
<title>Dulwick Medical — Business Cards</title>
<link rel="stylesheet" href="https://fonts.googleapis.com/css2?family=Raleway:wght@500;700&family=Roboto:wght@400&display=swap">
<style>
  :root {
    --navy: #0b2461;
    --blue: #2385bc;
    --white: #ffffff;
    --ink: #1a1a1a;
    --backdrop: #2a2b2f;
  }
  * { margin: 0; padding: 0; box-sizing: border-box; }
  html, body { width: 1200px; height: 900px; overflow: hidden; }
  body {
    background: var(--backdrop);
    font-family: "Raleway", sans-serif;
    position: relative;
  }
  .card {
    position: absolute;
    left: 290px;
    width: 620px;
    height: 354px;
    border-radius: 18px;
    overflow: hidden;
  }
  .card--front { top: 70px; background: var(--white); }
  .card--back { top: 476px; background: var(--navy); }

  .front-art { position: absolute; left: 0; top: 0; width: 620px; height: 354px; }

  .wordmark {
    position: absolute;
    top: 30px;
    right: 34px;
    display: flex;
    align-items: center;
    gap: 10px;
    color: var(--navy);
    font-weight: 700;
    font-size: 22px;
    letter-spacing: 1px;
    text-transform: uppercase;
  }
  .wordmark__square { width: 16px; height: 16px; background: var(--blue); }

  .accent-bar {
    position: absolute;
    right: 0;
    top: 118px;
    width: 14px;
    height: 36px;
    background: var(--navy);
  }

  .details {
    position: absolute;
    right: 42px;
    top: 114px;
    text-align: right;
  }
  .details__name {
    font-weight: 700;
    font-size: 24px;
    color: var(--navy);
    text-transform: uppercase;
  }
  .details__role {
    margin-top: 4px;
    font-weight: 500;
    font-size: 15px;
    color: var(--blue);
    text-transform: uppercase;
  }
  .contact {
    margin-top: 26px;
    font-family: "Roboto", sans-serif;
    font-size: 15px;
    color: var(--ink);
    line-height: 26px;
  }
  .contact__line { display: flex; justify-content: flex-end; align-items: center; gap: 10px; }
  .contact__icon { width: 16px; height: 16px; }

  .back-wordmark {
    position: absolute;
    inset: 0;
    display: flex;
    align-items: center;
    justify-content: center;
    gap: 14px;
    color: var(--white);
    font-weight: 700;
    font-size: 38px;
    letter-spacing: 2px;
    text-transform: uppercase;
  }
  .back-wordmark__square { width: 24px; height: 24px; background: var(--white); }
</style>
</head>
<body>

<section class="card card--front" aria-label="Business card front">
  <svg class="front-art" viewBox="0 0 620 354" role="img" aria-label="Large brand mark decoration in navy and blue">
    <defs>
      <linearGradient id="decorFill" x1="0" y1="0" x2="1" y2="1">
        <stop offset="0" stop-color="#0b2461"/>
        <stop offset="1" stop-color="#2385bc"/>
      </linearGradient>
    </defs>
    <path d="M0 150 L0 354 L330 354 Q300 260 260 150 Q200 90 120 100 Q60 110 0 150 Z" fill="url(#decorFill)"/>
  </svg>

  <div class="wordmark"><span class="wordmark__square"></span>Dulwick Medical</div>
  <div class="accent-bar"></div>

  <div class="details">
    <h1 class="details__name">Harriet Colbeck</h1>
    <p class="details__role">Director/Sales Agent</p>
    <div class="contact">
      <p class="contact__line">0461 835 207
        <svg class="contact__icon" viewBox="0 0 16 16" aria-hidden="true"><path d="M3 2h3l1 3-2 1a8 8 0 0 0 5 5l1-2 3 1v3a1 1 0 0 1-1 1A12 12 0 0 1 2 3a1 1 0 0 1 1-1z" fill="#2385bc"/></svg>
      </p>
      <p class="contact__line">harriet@dulwickmedical.com.au
        <svg class="contact__icon" viewBox="0 0 16 16" aria-hidden="true"><rect x="1" y="3" width="14" height="10" fill="#2385bc"/><path d="M1 3l7 6 7-6" fill="none" stroke="#fff" stroke-width="1.2"/></svg>
      </p>
    </div>
  </div>
</section>

<section class="card card--back" aria-label="Business card back">
  <div class="back-wordmark"><span class="back-wordmark__square"></span>Dulwick Medical</div>
</section>

</body>
</html>
```